Use your magic to make a startup company look established*

We are in need of a website that gives the appearance that we are established rather than new. Our audience is comprised of senior executives in technology professional services companies, financial people (conservative) that invest in them, and executives in companies that are in need of their services. The site therefore needs to lean towards the conservative side while being modern and professional.

This should be a fairly simple site.

- About us
- Services
- Contacts
- Content (Articles)

It should be SEO friendly and easy to add content or sub pages. A responsive design is mandatory.

Target Market(s)

We work with executives and investors in professional services companies to more effectively compete in the already crowded “digital transformation” market.

Industry/Entity Type

Professional Service

Coding

Coded - Design and coding required

Number of Pages Required

5+ page

Font styles to use
Sans Serif

Requirements
Must have
• - Responsive design
- Easy to add/change content
- Easy to add additional pages

```html
<!DOCTYPE html>
<html lang="en">
<head>
<meta charset="utf-8">
<title>Summit Crest Partners</title>
<link href="https://fonts.googleapis.com/css2?family=Lato:ital,wght@0,300;0,400;0,700;0,900;1,300&family=Montserrat:wght@400;500;600;700&display=swap" rel="stylesheet">
<style>
:root{
  --gold:#d5a34c;
  --gold-deep:#bf8d2c;
  --gold-grad:linear-gradient(180deg,#d8a94e 0%,#b8892d 100%);
  --nav:#47474a;
  --ink:#1c1c1c;
  --text:#555;
  --brand-grey:#6f6f6f;
  --soft:#f2f1f1;
  --soft-2:#efeeec;
  --footer:#1e1e1e;
  --bar:#46464a;
  --white:#fff;
}
*{box-sizing:border-box;margin:0;padding:0}
html,body{width:1200px;height:2482px;overflow:hidden;background:var(--white)}
body{font-family:'Lato',sans-serif;color:var(--text);position:relative}
section,header,nav,footer{position:relative;width:1200px}
.abs{position:absolute}
.label{font-family:'Lato',sans-serif;font-size:13px;color:var(--gold-deep);text-transform:uppercase;letter-spacing:.2px}
.title{font-family:'Lato',sans-serif;font-weight:700;color:var(--ink)}
.center{left:0;width:1200px;text-align:center}
.rule{height:3px;background:var(--gold-deep)}

/* top bar */
.topbar{height:123px}
.brand{left:123px;top:55px;display:flex;align-items:center;gap:10px}
.brand-dot{width:14px;height:14px;border-radius:50%;background:var(--gold);display:block}
.brand-name{font-family:'Lato',sans-serif;font-weight:700;font-size:20px;color:var(--brand-grey);white-space:nowrap}
.contact-item{font-family:'Montserrat',sans-serif;font-size:12px}
.contact-item .k{color:var(--gold-deep);font-weight:600;display:flex;align-items:center;gap:6px}
.contact-item .v{color:#333;font-weight:600;font-size:13px;padding-left:18px;margin-top:2px}
.contact-item .v.light{font-weight:400;color:#555;font-size:12px}
.follow{left:969px;top:50px;font-family:'Montserrat',sans-serif;font-size:12px;color:var(--gold-deep);font-weight:600}
.social{display:flex;gap:2px;margin-top:5px}
.social span{width:19px;height:19px;background:#4a4a4a;display:block}

/* nav */
.mainnav{height:43px;background:var(--nav)}
.mainnav a{position:absolute;top:0;line-height:43px;font-family:'Montserrat',sans-serif;font-weight:600;font-size:12.5px;color:var(--white);text-decoration:none;text-transform:uppercase}
.mainnav a.active{color:var(--gold)}
.mainnav a.cta{background:var(--gold-grad);width:165px;text-align:center}

/* hero */
.hero{height:576px}
.hero-art{left:135px;top:75px;width:424px;height:423px;background:radial-gradient(ellipse at 45% 45%,#d08b3f 0%,#c98a45 35%,#f1e4d6 62%,#ffffff 80%)}
.hero-lead{left:632px;top:72px;font-size:39px;font-weight:300;font-style:italic;color:#333}
.hero-head{left:632px;top:118px;font-family:'Lato',sans-serif;font-weight:900;font-size:59px;line-height:54px;color:var(--gold);text-transform:uppercase}
.hero-copy{left:643px;top:345px;font-size:20px;font-weight:300;line-height:23px;color:#333;width:380px}
.btn{display:inline-block;background:var(--gold-grad);color:var(--white);text-decoration:none;text-align:center}
.hero-btn{left:644px;top:424px;width:148px;height:42px;line-height:42px;font-size:14px}

/* about */
.about{height:378px;background:var(--soft)}
.about .copy{font-size:12.5px;line-height:15.5px;color:#444;width:940px}
.pill{left:540px;top:285px;width:108px;height:35px;line-height:35px;border-radius:18px;font-family:'Montserrat',sans-serif;font-weight:700;font-size:9px;letter-spacing:1px}

/* services */
.services{height:591px}
.services .intro{left:130px;top:170px;width:940px;text-align:center;font-size:12.5px;line-height:20px;color:#444}
.card{top:235px;width:310px}
.card-img{height:164px}
.card h3{font-family:'Montserrat',sans-serif;font-weight:700;font-size:13.5px;color:var(--ink);margin-top:32px}
.card p{font-size:12.5px;line-height:15.5px;color:#666;margin-top:15px;width:290px}
.card .more{display:block;margin-top:16px;font-family:'Montserrat',sans-serif;font-weight:700;font-size:10px;color:var(--gold-deep);text-decoration:none}

/* testimonials / articles */
.split{height:429px;background:var(--soft-2)}
.quote-mark{left:126px;top:168px;font-family:'Lato',sans-serif;font-weight:900;font-size:64px;line-height:64px;color:var(--gold)}
.quote{left:126px;top:215px;width:459px;font-size:12.5px;line-height:15.5px;color:#555;text-align:justify}
.author{left:122px;top:324px;font-size:13px;color:var(--gold-deep)}
.dots{left:125px;top:355px;display:flex;gap:5px}
.dots i{width:6px;height:6px;border-radius:50%;background:#aaa;display:block}
.dots i.on{background:var(--gold)}
.post{left:652px;width:440px;display:flex;gap:16px}
.date{width:42px;flex:none}
.date .d{height:33px;background:var(--gold);color:var(--white);font-size:23px;text-align:center;line-height:35px}
.date .m{height:19px;background:var(--ink);color:var(--white);font-family:'Montserrat',sans-serif;font-size:10.5px;text-align:center;line-height:19px}
.post h4{font-family:'Lato',sans-serif;font-weight:700;font-size:14.5px;color:var(--gold);margin-top:-3px;white-space:nowrap}
.post p{font-size:12.5px;line-height:16px;color:#777;margin-top:5px}
.art-btn{left:653px;top:337px;width:107px;height:33px;line-height:33px;font-size:14px;font-family:'Montserrat',sans-serif;background:var(--gold)}

/* footer */
.footer{height:296px;background:var(--footer)}
.f-brand{left:114px;top:68px;display:flex;align-items:center;gap:9px}
.f-brand .brand-dot{width:12px;height:12px}
.f-brand .brand-name{font-size:17px;color:#ddd}
.f-about{left:111px;top:126px;width:266px;font-family:'Montserrat',sans-serif;font-size:11.5px;line-height:15.5px;color:#ddd}
.f-social{left:114px;top:217px;display:flex;gap:3px}
.f-social span{width:21px;height:21px;background:var(--gold);display:block}
.f-head{top:65px;font-family:'Montserrat',sans-serif;font-weight:700;font-size:13px;color:var(--gold)}
.f-list{list-style:none;font-family:'Montserrat',sans-serif;font-size:12px;color:#ddd}
.quick{left:457px;top:98px}
.quick li{height:23.6px;display:flex;align-items:center;gap:10px}
.quick li::before{content:"";width:0;height:0;border-left:7px solid var(--gold);border-top:4px solid transparent;border-bottom:4px solid transparent}
.doing{left:644px;top:95px;width:156px}
.doing li{height:25.4px;line-height:25px;border-bottom:1px solid #ddd}
.doing li:last-child{border-bottom:none}
.f-contact{left:870px;top:104px;font-family:'Montserrat',sans-serif;font-size:12px;line-height:15.5px;color:#ddd}
.f-contact .row{display:flex;gap:10px;position:absolute;left:0;white-space:nowrap}
.f-contact svg{flex:none;margin-top:1px}
.copyright{height:46px;background:var(--bar);text-align:center;line-height:46px;font-family:'Montserrat',sans-serif;font-size:12px;color:#ddd}
</style>
</head>
<body>

<header class="topbar">
  <div class="abs brand">
    <span class="brand-dot" aria-hidden="true"></span>
    <span class="brand-name">Summit Crest Partners</span>
  </div>
  <div class="abs contact-item" style="left:414px;top:53px">
    <div class="k"><svg width="12" height="12" viewBox="0 0 24 24"><path fill="#bf8d2c" d="M6.6 10.8a15.1 15.1 0 0 0 6.6 6.6l2.2-2.2c.3-.3.7-.4 1-.2 1.1.4 2.3.6 3.6.6.6 0 1 .4 1 1V20c0 .6-.4 1-1 1A17 17 0 0 1 3 4c0-.6.4-1 1-1h3.5c.6 0 1 .4 1 1 0 1.3.2 2.5.6 3.6.1.3 0 .7-.2 1z"/></svg>Call Us Now</div>
    <div class="v">+ (555) 014-2290</div>
  </div>
  <div class="abs contact-item" style="left:644px;top:53px">
    <div class="k"><svg width="13" height="10" viewBox="0 0 26 20"><rect width="26" height="20" fill="#bf8d2c"/><path d="M1 2l12 9 12-9" stroke="#fff" stroke-width="2" fill="none"/></svg>Contact Email</div>
    <div class="v light" style="padding-left:22px">info@summitcrestpartners.com</div>
  </div>
  <div class="abs follow">Follow Us
    <div class="social" aria-label="Social links"><span></span><span></span><span></span><span></span><span></span></div>
  </div>
</header>

<nav class="mainnav">
  <a class="active" href="#" style="left:134px">Home</a>
  <a href="#" style="left:246px">About Us</a>
  <a href="#" style="left:372px">Services</a>
  <a href="#" style="left:501px">Our Team</a>
  <a href="#" style="left:638px">Blog</a>
  <a href="#" style="left:744px">Content</a>
  <a href="#" style="left:856px">Contact Us</a>
  <a class="cta" href="#" style="left:969px">Make Appointment</a>
</nav>

<section class="hero">
  <div class="abs hero-art" role="img" aria-label="Large copper arrow curving upward, pushed by a businessman"></div>
  <p class="abs hero-lead">We help you invest in</p>
  <h1 class="abs hero-head">Technology<br>Professional<br>Services<br>Companies</h1>
  <p class="abs hero-copy">At cum veri epicurei constituto, legendos maluisset ne vis. Nam nulla incorrupte id.</p>
  <a class="abs btn hero-btn" href="#">Contact us</a>
</section>

<section class="about">
  <p class="abs center label" style="top:61px">About us</p>
  <h2 class="abs center title" style="top:80px;font-size:33px">Welcome to Summit Crest Partners</h2>
  <p class="abs copy" style="left:124px;top:152px">Lorem ipsum dolor sit amet, cu per porro dolore nostro, partem integre corpora per ea, tation ornatus mel ad. Brute voluptatibus an est, per cu utroque torquatos, ei eum amet hinc. Ne vix ludus timeam definitionem. His hinc dicunt minimum cu, qui te dico laoreet. Sea ea mucius diceret solens, eos ei nostrud appellantur, an autem vocent novum doctus id mel. Id everti commune accusata melsunt explicabo. Nemo enim ipsam voluptatem quia voluptas sit aspernatur aut odit aut fugit,</p>
  <p class="abs copy" style="left:124px;top:214px">sed quia consequuntur magni dolores eos qui ratione voluptatem sequi nesciunt. Neque porro quisquam est, qui dolorem ipsum quia dolor sit amet, consectetur, adipisci velit, sed quia non numquam eius modi tempora incidunt ut labore et dolore magnam aliquam</p>
  <a class="abs btn pill" href="#">READ MORE</a>
</section>

<section class="services">
  <p class="abs center label" style="top:73px">Viderer nostrud an est</p>
  <h2 class="abs center title" style="top:90px;font-size:34px">Our Main Services</h2>
  <div class="abs rule" style="left:553px;top:139px;width:81px"></div>
  <p class="abs intro">quo in errem diceret tincidunt. Usu te alii argumentum, vis ea platonem reprehendunt. Et liber nostrud temporibus mei, viderer nostrud an est. Splendide definitionem at pro. Ut sit putant legimus an viris scripta deterruisset sit. Ad movet labitur reprimique cum, no his qualisque consetetur.</p>

  <article class="abs card" style="left:102px">
    <div class="card-img" role="img" aria-label="Pen resting on printed financial reports" style="background:linear-gradient(135deg,#eef1f4,#d8dfe6 60%,#bcd3e6)"></div>
    <h3>INVESTMENT SERVICES</h3>
    <p>Lorem ipsum dolor sit amet, consectetur adipiscing elit, sed do eiusmod tempor incididunt ut labore et vis ea platonem reprehendunt.</p>
    <a class="more" href="#">READ MORE</a>
  </article>
  <article class="abs card" style="left:444px">
    <div class="card-img" role="img" aria-label="Colourful printed charts and graphs spread on a desk" style="background:linear-gradient(135deg,#f1ede2,#e7c86a 45%,#5b8fc0)"></div>
    <h3 style="margin-left:3px">FINANCIAL SERVICES</h3>
    <p style="margin-left:5px">Lorem ipsum dolor sit amet, consectetur adipiscing elit, sed do eiusmod tempor incididunt ut labore et vis ea platonem reprehendunt.</p>
    <a class="more" href="#" style="margin-left:3px">READ MORE</a>
  </article>
  <article class="abs card" style="left:785px">
    <div class="card-img" role="img" aria-label="Tablet showing blue business dashboards" style="background:linear-gradient(135deg,#3a8cc7,#e8eef3 45%,#2f7fb9)"></div>
    <h3 style="margin-left:4px">CUSTOMER SERVICES</h3>
    <p style="margin-left:4px">Lorem ipsum dolor sit amet, consectetur adipiscing elit, sed do eiusmod tempor incididunt ut labore et vis ea platonem reprehendunt.</p>
    <a class="more" href="#" style="margin-left:4px">READ MORE</a>
  </article>
</section>

<section class="split">
  <p class="abs label" style="left:120px;top:86px">Testimonials</p>
  <h2 class="abs title" style="left:123px;top:102px;font-size:33px">What Client Says</h2>
  <div class="abs rule" style="left:125px;top:144px;width:56px"></div>
  <div class="abs quote-mark" aria-hidden="true">&ldquo;</div>
  <p class="abs quote">Duo Reges: constructio interrete. Quia nec honesto quic quam honestius nec turpi turpius. Tria genera bonorum; Quid iudicant sensus? Quae qui non vident, nihil umquam magnum ac cognitione dignum amaverunt. Dicet pro me ipsa virtus nec dubitabit isti vestro beato M. Nihil ad rem! Ne sit sane; qui non vident, nihil umquam magnum ac cognitione dignum amaverunt. quam honestius nec turpi turpius. Tria genera bonorum</p>
  <p class="abs author">-Martin</p>
  <div class="abs dots"><i class="on"></i><i></i><i></i></div>

  <p class="abs label" style="left:655px;top:86px">Ostrud an est</p>
  <h2 class="abs title" style="left:652px;top:102px;font-size:33px">Articles</h2>
  <div class="abs rule" style="left:653px;top:144px;width:56px"></div>
  <article class="abs post" style="top:169px">
    <div class="date"><div class="d">05</div><div class="m">JAN</div></div>
    <div><h4>Porro dolore nostro Lorem ipsum dolor sit ametcu per</h4><p>Lorem ipsum dolor sit amet, cu per porro dolore nostro, partem integre corpora per ea, tation ornatus mel ad Brute</p></div>
  </article>
  <article class="abs post" style="top:250px">
    <div class="date"><div class="d">03</div><div class="m">JAN</div></div>
    <div><h4>Dlore nostro Lorem ipsum dolor sit ametcu per nostro</h4><p>Lorem ipsum dolor sit amet, cu per porro dolore nostro, partem integre corpora per ea, tation ornatus mel ad Brute</p></div>
  </article>
  <a class="abs btn art-btn" href="#">Read more</a>
</section>

<footer class="footer">
  <div class="abs f-brand">
    <span class="brand-dot" aria-hidden="true"></span>
    <span class="brand-name">Summit Crest Partners</span>
  </div>
  <p class="abs f-about">Lorem ipsum dolor sit amet, cu per porro dolore nostro, partem integre corpora per ea, tation ornatus mel ad. Brute voluptatibus an est, per cu utroque torquatos, ei eum amet hinc.</p>
  <div class="abs f-social" aria-label="Social links"><span></span><span></span><span></span><span></span><span></span></div>

  <h5 class="abs f-head" style="left:457px">Quick Link</h5>
  <ul class="abs f-list quick">
    <li>About us</li><li>Services</li><li>Our Team</li><li>Blog</li><li>Content</li><li>Contact us</li>
  </ul>

  <h5 class="abs f-head" style="left:644px;top:64px">What We do</h5>
  <ul class="abs f-list doing">
    <li>Epicurei constituto</li><li>Legendos maluisset</li><li>Usu te alii argumentum</li><li>Labitur reprimique</li><li>Dolorum adolescens</li><li>Discere antiopam</li>
  </ul>

  <h5 class="abs f-head" style="left:870px">Contact info</h5>
  <div class="abs f-contact">
    <div class="row" style="top:0"><svg width="12" height="15" viewBox="0 0 24 30"><path fill="#d5a34c" d="M12 0a11 11 0 0 0-11 11c0 8 11 19 11 19s11-11 11-19A11 11 0 0 0 12 0zm0 15a4 4 0 1 1 0-8 4 4 0 0 1 0 8z"/></svg><span>Summit Crest Partners<br>4210 Harbor Lane<br>Millbrook, USA</span></div>
    <div class="row" style="top:70px;font-weight:600"><svg width="13" height="13" viewBox="0 0 24 24"><path fill="#d5a34c" d="M6.6 10.8a15.1 15.1 0 0 0 6.6 6.6l2.2-2.2c.3-.3.7-.4 1-.2 1.1.4 2.3.6 3.6.6.6 0 1 .4 1 1V20c0 .6-.4 1-1 1A17 17 0 0 1 3 4c0-.6.4-1 1-1h3.5c.6 0 1 .4 1 1 0 1.3.2 2.5.6 3.6.1.3 0 .7-.2 1z"/></svg><span>+ (555) 014-2290</span></div>
    <div class="row" style="top:100px"><svg width="13" height="10" viewBox="0 0 26 20" style="margin-top:3px"><rect width="26" height="20" fill="#d5a34c"/><path d="M1 2l12 9 12-9" stroke="#1e1e1e" stroke-width="2" fill="none"/></svg><span>info@summitcrestpartners.com</span></div>
  </div>
</footer>

<div class="copyright">Copyright 2020, Summit Crest Partners, All Right Reserved</div>

</body>
</html>
```